Residential Mortgage Leader needs Wordpress Design

Looking for a home page website design for a client. We develop using the WordPress platform and would prefer the design be at least loosely based on an existing WordPress template. Attached files have many notes from our creative brief with client. The site must be responsive. Approved, basic wireframe attached. There is room for interpretation.

Existing web site: http://www.marisolbrandt.example/

The Marisol Brandt Team relies on strong systems to deliver an on-time, done-right, friendly experience. Marisol offers mortgages and refinancing services throughout the United States. She is a successful Brightwillow Lending agent who strives to be an active part of her community. She would like to focus the site on her team, rather than just her.

Difference makers...
When you work with the Marisol Brandt team you get a high level of expertise and a friendly experience.

She has amazing credentials. Marisol is widely recognized as a top producer for her company, and has earned a number of awards and honors for her customer service.

Marisol's team is very engaged and enjoys sharing social comments or photos from their community.

Imagery:
* Friendly, warm imagery, preferably of her team or an image to represent her team
* Clean and crisp
* Professional / Experts in mortgage and refinance
* Clean / Good use of white space
Updates

When possible, please use imagery from the DFW area. The client mentioned they would prefer not to see stock images. Thanks.

Amend that- creative use of stock images, however, is fine. A few designs have used stock imagery, but in a well-considered manner.

We added some photos and graphics that are local. We are Dallas / Ft. Worth, Plano, Frisco, Texas. We also added some examples of photos to use for the "In the Community" area. Stock photos of business folks just doesn't fit there. Thanks!

Target Market(s)

They service a lot of builders, but also work with homeowners. Their typical client is usually a woman searching for mortgage services online. She typically has a family and may refer her husband to Marisol's team. Keep in mind, however, they also see a number of other scenarios. Most of their clients are middle to high-end borrowers.

Industry/Entity Type

It Company

Requirements
Must have
• Design should be developed using program such as Photoshop or Fireworks or Illustrator as last preference. Ideally, the design would be based on an existing responsive WordPress theme, which we would customize. You must include the name of the target theme. The footer should include lots of space for disclaimers and legal language. Site navigation should include these choices: "Home, About, Builders, Mortgage Info, Approval, Blog, Contact"
Nice to have
• Blog, social media and photos area. Use of the already approved style prototype with colors and fonts (Lato- a Google font, Times New Roman and Cookie-a decorative Google font). However, we are open to interpretation.
Should not have
• Hard to read fonts or a lack of white space.

```html
<!DOCTYPE html>
<html lang="en">
<head>
<meta charset="utf-8">
<title>Brightwillow Lending – Marisol Brandt Team</title>
<link rel="stylesheet" href="https://fonts.googleapis.com/css2?family=Cookie&family=Lato:wght@300;400;700&family=Tinos&display=swap">
<style>
:root{
  --red:#c42a1c;
  --red-btn:#c9301f;
  --blue:#1f86bf;
  --blue-btn:#2b8fcc;
  --text:#555;
  --muted:#6a6a6a;
  --dark:#3a3a3a;
  --hero-bg:#edf2f5;
  --frame:#d3dbe1;
  --footer:#dcdcdc;
  --footer-bar:#cbcbcb;
  --line:#dedede;
}
*{margin:0;padding:0;box-sizing:border-box}
html,body{width:930px;height:1200px;overflow:hidden;background:#fff}
body{font-family:'Lato',sans-serif;color:var(--text);position:relative}
.abs{position:absolute}

/* header */
.site-header{top:0;left:0;width:930px;height:78px;border-bottom:1px solid #555}
.brand{left:85px;top:22px}
.brand-name{font-size:25px;font-weight:700;color:var(--red);letter-spacing:-.3px;display:flex;align-items:center;gap:8px}
.brand-mark{width:14px;height:14px;background:var(--red);border-radius:50%}
.brand-tag{font-size:11px;font-weight:700;color:var(--dark);margin-top:1px}
.work{left:700px;top:18px;display:flex;gap:8px}
.work small{display:block;font-size:12px;color:var(--dark)}
.work strong{display:block;font-size:14px;font-weight:400;color:var(--red)}

/* nav */
.main-nav{top:79px;left:0;width:930px;height:43px}
.main-nav a{position:absolute;top:15px;font-size:12.5px;color:#444;text-decoration:none}
.main-nav a.current{color:var(--red)}

/* hero */
.hero{top:122px;left:0;width:930px;height:346px;background:radial-gradient(circle at 50% 0,#f6f8fa,var(--hero-bg) 70%)}
.hero-photo{left:109px;top:39px;width:375px;height:256px;background:var(--frame);padding:5px}
.hero-photo div{width:100%;height:100%;background:linear-gradient(160deg,#9fb3c5,#6f8aa8 45%,#8aa19a 80%,#b7c3c9)}
.hero-title{left:514px;top:34px;font-family:'Cookie',cursive;font-size:43px;color:var(--blue);font-weight:400}
.hero-copy{left:516px;width:295px;font-size:10.4px;line-height:14px;color:var(--text);font-weight:400}
.btn{position:absolute;color:#fff;font-family:'Tinos','Times New Roman',serif;display:flex;align-items:center;justify-content:center;text-decoration:none}
.btn-blue{left:515px;top:247px;width:118px;height:35px;background:var(--blue-btn);font-size:14.5px}

/* widgets */
.widget-title{position:absolute;font-family:'Tinos','Times New Roman',serif;font-size:19.5px;color:var(--red);font-weight:400}
.copy{position:absolute;font-size:9.8px;line-height:14px;color:var(--muted);font-weight:400}
.btn-red{left:101px;top:662px;width:86px;height:31px;background:var(--red-btn);font-size:13.5px}
.framed{position:absolute;width:170px;height:124px;background:var(--frame);padding:5px}
.framed div{width:100%;height:100%}

.post{position:absolute;left:101px;width:300px;height:66px}
.post .date{position:absolute;left:0;top:0;width:32px;text-align:center;font-family:'Tinos','Times New Roman',serif;color:var(--dark);line-height:1}
.post .date b{display:block;font-size:29px;font-weight:400}
.post .date span{display:block;font-size:12.5px;margin-top:2px}
.post .date i{display:block;font-size:12.5px;font-style:normal;margin-top:3px}
.post .body{position:absolute;left:38px;top:0;height:64px;border-left:1px solid var(--line);padding-left:8px}
.post h3{font-size:13.5px;font-weight:400;color:var(--dark);margin-left:-1px}
.post p{font-size:9.6px;line-height:14px;color:var(--muted);font-weight:400;margin-top:2px}
.post em{display:block;font-style:normal;font-size:8px;color:var(--muted);margin-top:2px}

.social{left:441px;top:749px;width:169px;list-style:none}
.social li{height:25px;border-bottom:1px solid var(--line);font-size:12px;color:#555;padding-top:3px}
.thumb{position:absolute;width:82px;height:68px;border:1px solid #e4e4e4}

/* footer */
.site-footer{top:926px;left:0;width:930px;height:229px;background:var(--footer)}
.foot-title{position:absolute;top:30px;font-size:14px;font-weight:700;color:var(--dark)}
.foot-list{position:absolute;list-style:none;font-size:10px;line-height:17.8px;color:#555}
.lang{left:339px;top:179px;width:84px;height:26px;background:#fff;border:1px solid #ccc;font-size:10px;color:#333;padding:6px 0 0 8px}
.lang svg{position:absolute;right:6px;top:9px}
.agent-photo{left:582px;top:32px;width:113px;height:128px;background:linear-gradient(170deg,#7a5443,#3a2a24 70%,#1e1816)}
.agent-name{left:702px;top:32px;font-size:14px;font-weight:700;color:var(--dark);line-height:17px}
.agent-info{left:703px;top:70px}
.footer-bar{top:1155px;left:0;width:930px;height:45px;background:var(--footer-bar)}
.copyright{left:101px;top:18px;font-size:10px;color:#555}
.social-icons{left:704px;top:9px;display:flex;gap:3px}
.social-icons span{width:27px;height:27px;border-radius:3px}
</style>
</head>
<body>

<header class="site-header abs">
  <div class="brand abs">
    <div class="brand-name">Brightwillow Lending<span class="brand-mark"></span></div>
    <div class="brand-tag">A Lonestar Holdings Company</div>
  </div>
  <div class="work abs">
    <svg width="26" height="34" viewBox="0 0 26 34" fill="none" stroke="#333" stroke-width="2">
      <path d="M4 18 V13 a9 9 0 0 1 18 0 V18"/>
      <rect x="2" y="15" width="5" height="9" rx="2" fill="#333"/>
      <rect x="19" y="15" width="5" height="9" rx="2" fill="#333"/>
      <path d="M5 24 q2 7 10 7"/><circle cx="16" cy="31" r="1.6" fill="#333"/>
    </svg>
    <div><small>Work With Us:</small><strong>0800-555-0142</strong></div>
  </div>
</header>

<nav class="main-nav abs">
  <a class="current" href="#" style="left:108px">Home</a>
  <a href="#" style="left:208px">About Us</a>
  <a href="#" style="left:319px">Builders</a>
  <a href="#" style="left:410px">Mortgage Info</a>
  <a href="#" style="left:534px">Approval</a>
  <a href="#" style="left:654px">Blog</a>
  <a href="#" style="left:745px">Contact Us</a>
</nav>

<section class="hero abs">
  <div class="hero-photo abs"><div role="img" aria-label="Smiling couple sitting by a poolside home"></div></div>
  <h1 class="hero-title abs">Earning Your Business</h1>
  <p class="hero-copy abs" style="top:95px">Lorem ipsum dolor sit amet, consectetur adipisicing elit, sed do eiusmod tempor incididunt ut labore et dolore magna aliqua.</p>
  <p class="hero-copy abs" style="top:137px">&nbsp;Ut enim ad minim veniam, quis nostrud exercitation ullamco laboris nisi ut aliquip ex ea commodo consequat. Duis aute irure dolorpariatur.</p>
  <p class="hero-copy abs" style="top:193px">Excepteur sint occaecat cupidatat non proident, sunt in culpa qui officia deserunt mollit anim id est laborum.</p>
  <a class="btn btn-blue" href="#">Get to Know Us</a>
</section>

<main>
  <h2 class="widget-title" style="left:101px;top:494px">Our Credentials</h2>
  <p class="copy" style="left:101px;top:528px;width:295px">Lorem ipsum dolor sit amet, consectetur adipisicing elit, sed do eius-mod tempor incididunt ut labore et dolore magna aliqua. Ut enim ad minim veniam, quis nostrud exercitation ullamco laboris nisi ut aliquip ex ea commodo consequat.</p>
  <p class="copy" style="left:101px;top:592px;width:295px">Duis aute irure dolor in reprehenderit in voluptate velit esse cillum dolore eu fugiat nulla pariatur. Excepteur sint occaecat cupidatat non proident, sunt in culpa qui officia deserunt mollit anim id est laborum....</p>
  <a class="btn btn-red" href="#">Read More</a>

  <h2 class="widget-title" style="left:441px;top:494px">Awards</h2>
  <div class="framed" style="left:441px;top:530px"><div role="img" aria-label="Readers' choice award ribbon badge" style="background:linear-gradient(135deg,#e9e9e9,#c9ccd4 50%,#6f86c4)"></div></div>
  <p class="copy" style="left:441px;top:665px;width:170px">Lorem ipsum dolor sit amet, consecte-tur adipisicing elit...</p>

  <h2 class="widget-title" style="left:661px;top:494px">Recognion</h2>
  <div class="framed" style="left:661px;top:530px"><div role="img" aria-label="Colorful circle of star figures illustration" style="background:radial-gradient(circle,#fff 25%,#f4c54a 45%,#7fc6d8 65%,#fff 80%)"></div></div>
  <p class="copy" style="left:661px;top:665px;width:170px">Lorem ipsum dolor sit amet, consecte-tur adipisicing elit...</p>

  <h2 class="widget-title" style="left:101px;top:719px">Blog</h2>
  <article class="post" style="top:754px">
    <div class="date"><b>2</b><span>Sep</span><i>2013</i></div>
    <div class="body"><h3>Bomowing</h3><p>Lorem ipsum dolor sit amet, consectetur adipisicing elit,<br>sed do eiusmod tempor...</p><em>2 comments</em></div>
  </article>
  <article class="post" style="top:831px">
    <div class="date"><b>10</b><span>Sep</span><i>2013</i></div>
    <div class="body"><h3>Best Practices</h3><p>Lorem ipsum dolor sit amet, consectetur adipisicing elit,<br>sed do eiusmod tempor...</p><em>2 comments</em></div>
  </article>

  <h2 class="widget-title" style="left:441px;top:719px">Social Media</h2>
  <ul class="social abs">
    <li>Subcribe Feeds</li>
    <li>Our Neighborly Page</li>
    <li>Follow Us On Chirpline</li>
    <li>Snapfolio</li>
    <li>Workline</li>
  </ul>

  <h2 class="widget-title" style="left:661px;top:719px">In The Community</h2>
  <div class="thumb" role="img" aria-label="Large group of children and families" style="left:661px;top:754px;background:linear-gradient(160deg,#6a9fd0,#e0a45a 60%,#4a6fa3)"></div>
  <div class="thumb" role="img" aria-label="Team members standing together" style="left:749px;top:754px;background:linear-gradient(160deg,#7fa8c9,#3b4550 60%,#1f2530)"></div>
  <div class="thumb" role="img" aria-label="Stacked hands of community volunteers" style="left:661px;top:828px;background:linear-gradient(160deg,#d66aa2,#e8b48e 50%,#9cc46a)"></div>
  <div class="thumb" role="img" aria-label="Group at a local building entrance" style="left:749px;top:828px;background:linear-gradient(160deg,#b9c2cf,#7a6a66 55%,#d9dde3)"></div>
</main>

<footer class="site-footer abs">
  <h4 class="foot-title" style="left:101px">LINKS</h4>
  <ul class="foot-list" style="left:101px;top:62px">
    <li>Home</li><li>About</li><li>Builders</li><li>Mortgage Info</li><li>Approval</li><li>Blog</li><li>Contact Us</li>
  </ul>
  <h4 class="foot-title" style="left:338px">ADDRESS</h4>
  <ul class="foot-list" style="left:339px;top:62px">
    <li>Our Address</li>
    <li>Corporate Office - 2400 Cedar Ridge Road,</li>
    <li>Suite 700 Dallas, Texas 75240</li>
    <li>&nbsp;</li>
    <li>Tel : 1-800-555-0199</li>
    <li>Email : Contact Brightwillow Lending</li>
  </ul>
  <div class="lang abs">Language...
    <svg width="9" height="6" viewBox="0 0 9 6"><path d="M1 1 L4.5 4.5 L8 1" fill="none" stroke="#444" stroke-width="1.3"/></svg>
  </div>
  <div class="agent-photo abs" role="img" aria-label="Portrait of the branch manager"></div>
  <div class="agent-name abs">Marisol Brandt<br>Branch Manager</div>
  <ul class="foot-list agent-info">
    <li>Office: 469.555.0148</li>
    <li>Cell: 866.555.0173</li>
    <li>mbrandt@brightwillow.example</li>
    <li>NMLS: 40218</li>
    <li>4820 Elm Commons , Ste. 210</li>
    <li>Frisco, TX 75033</li>
    <li>&nbsp;</li>
    <li>Directions</li>
  </ul>
</footer>

<div class="footer-bar abs">
  <p class="copyright abs">Copyright © 2013 Brightwillow Lending. All Rights Reserved</p>
  <div class="social-icons abs">
    <span style="background:#5ec2e6"></span>
    <span style="background:#3b5a98"></span>
    <span style="background:#e8702a"></span>
    <span style="background:#e6e6e6;border:1px solid #aaa"></span>
  </div>
</div>

</body>
</html>
```